依頼詳細
作成はレスポンシブウェブデザインにて作成をしようと考えているのですが、
SEOにも配慮したデザインを希望してます。

WEBサイトの雰囲気としては
http://lumivane.com/
上記のようなテイストを希望しています。
また、医療機関であり、患者さんがすぐに欲しい情報にたどり着けるよう
http://www.kozuetani-hp.or.jp/
上記のURLのような配置であれば診療時間やアクセスなどにすぐたどり着けて患者さんにとって利便性が高いと考えています。

・基本的に現行のサイトのページは全てリニューアルサイトに盛り込む予定
・基礎的なSEOを考慮して文字に関しては極力テキストで入れることを想定
・レスポンシブウェブデザインを前提としたデザイン

した上で、デザインをお願いできれば幸いです。
サイトURL
http://www.sorvane-dc.jp/
ページ数
2ページ
希望イメージ
シンプル 複雑
単色 カラフル
暗い 明るい
日常 高級
遊び心 厳粛
未来的 伝統的
女性的 男性的
希望する色
白をベースに清潔感かつモダンなイメージ
納品ファイル
• 高解像度JPG (.jpg)
• イラストレーター形式 (.ai)
補足説明

SEOを考えたときにある程度文字を入れるスペースを欲しかったので、そのような部分も確保しつつサイトのデザインが私のイメージに最も近かったので選ばせて頂きました。

皆様からの多数のご応募ありがとうございました。また次の機会もありましたらよろしくお願い致します。

```html
<!DOCTYPE html>
<html lang="ja">
<head>
<meta charset="utf-8">
<title>ソルヴェイン歯科クリニック｜医院のご紹介</title>
<link href="https://fonts.googleapis.com/css2?family=Noto+Sans+JP:wght@400;500;700&display=swap" rel="stylesheet">
<style>
:root{
  --green:#3aab47;
  --green-dark:#2c8e38;
  --green-soft:#e6f4e3;
  --line:#cfe6cb;
  --text:#444;
  --muted:#777;
  --bg:#ffffff;
}
*{box-sizing:border-box;margin:0;padding:0}
html,body{width:886px;height:1200px;overflow:hidden;background:var(--bg)}
body{font-family:"Noto Sans JP",sans-serif;color:var(--text);font-size:12px;position:relative}
a{color:inherit;text-decoration:none}

.site-header{position:absolute;left:0;top:0;width:886px;height:180px;background:linear-gradient(#fff,#f3faf1)}
.brand{position:absolute;left:22px;top:22px;color:var(--green)}
.brand-en{font-size:38px;font-weight:700;line-height:1.05;letter-spacing:.5px}
.brand-ja{font-size:15px;font-weight:500;margin-top:6px}
.brand-mark{display:inline-block;width:22px;height:22px;background:var(--green);border-radius:50%;vertical-align:middle;margin-right:8px}
.header-photo{position:absolute;left:430px;top:0;width:270px;height:180px;background:linear-gradient(135deg,#d9e8e4,#c9a878 60%,#eae2d0)}
.header-contact{position:absolute;left:712px;top:14px;width:162px;height:150px;border:2px solid var(--green);border-radius:6px;background:#fff;padding:10px 10px;text-align:center}
.contact-label{display:flex;align-items:center;gap:6px;color:var(--green);font-weight:700;font-size:13px}
.icon-phone{width:20px;height:20px;flex:0 0 20px}
.contact-tel{font-size:19px;font-weight:700;color:#333;margin:18px 0 22px;white-space:nowrap}
.btn{display:block;background:var(--green);color:#fff;border-radius:4px;font-weight:500;text-align:center}
.header-contact .btn{padding:7px 0;font-size:13px}

.header-rule{position:absolute;left:0;top:180px;width:886px;height:6px;background:var(--green)}

.sidebar{position:absolute;left:12px;top:200px;width:210px}
.global-nav li{list-style:none;display:flex;justify-content:space-between;align-items:center;border-bottom:1px solid var(--line);padding:12px 4px;font-size:14px;font-weight:500}
.arrow{width:20px;height:20px}
.side-box{border:2px solid var(--green);border-radius:6px;margin-top:20px;padding:10px}
.side-box h3{display:flex;align-items:center;gap:6px;color:var(--green);font-size:13px;font-weight:700}
.side-tel{font-size:22px;font-weight:700;color:#333;margin:6px 0 10px;white-space:nowrap}
.map{height:96px;background:linear-gradient(135deg,#eceee8,#d8dfd2);border:1px solid #ddd}
.address{font-size:10px;color:var(--muted);line-height:1.5;margin:8px 0}
.side-box .btn{padding:6px 0;font-size:11px}
.hours-title{background:var(--green);color:#fff!important;margin:-10px -10px 10px;padding:8px 10px;border-radius:3px 3px 0 0}
.hours{width:100%;border-collapse:collapse;font-size:10px;margin-bottom:10px}
.hours th,.hours td{border:1px solid var(--line);padding:5px 3px;text-align:center;font-weight:400}
.hours th{background:var(--green-soft)}
.blog-banner{margin-top:30px;height:58px;background:var(--green);border-radius:6px;color:#fff;display:flex;align-items:center;gap:12px;padding-left:18px;font-size:24px;font-weight:700}
.blog-banner span{width:28px;height:28px;background:#fff;border-radius:50%}

.main{position:absolute;left:238px;top:200px;width:636px}
.page-title{display:flex;align-items:center;gap:10px;font-size:18px;font-weight:700;color:var(--green);border-bottom:2px solid var(--green);padding-bottom:8px}
.page-title i{width:6px;height:22px;background:var(--green)}
.section{border:1px solid var(--line);border-radius:6px;margin-top:18px;padding:0 16px 18px}
.section h2{font-size:15px;font-weight:700;color:#333;padding:12px 0;border-bottom:1px dashed var(--line);margin-bottom:16px}
.row{display:flex;gap:20px}
.building-photo{flex:0 0 230px;height:200px;background:linear-gradient(#cfdde8,#b9bbb8 55%,#8d8f8a)}
.text p{font-size:12.5px;line-height:1.9;margin-bottom:10px}
.lead{font-size:12.5px;line-height:1.9;margin-top:12px}
.doctor-photo{width:190px;height:170px;background:linear-gradient(#dfe6ea,#aab4bb)}
.doctor-note{font-size:10px;color:var(--muted);line-height:1.6;margin-top:8px;width:190px}
.career{flex:1;list-style:none}
.career li{border-bottom:1px dotted #ccc;padding:7px 0 7px 16px;font-size:12.5px;position:relative}
.career li:before{content:"";position:absolute;left:2px;top:13px;width:7px;height:7px;background:var(--green);border-radius:50%}

.site-footer{position:absolute;left:0;top:1118px;width:886px}
.footer-links{text-align:center;font-size:11px;color:var(--muted);padding:10px 0}
.copyright{background:var(--green);color:#fff;text-align:center;font-size:11px;height:52px;line-height:52px}
</style>
</head>
<body>

<header class="site-header">
  <div class="brand">
    <div class="brand-en">Sorvane<br>Dental Clinic</div>
    <div class="brand-ja"><span class="brand-mark"></span>ソルヴェイン歯科クリニック</div>
  </div>
  <div class="header-photo" role="img" aria-label="院内のキリンの置物と窓辺の写真"></div>
  <div class="header-contact">
    <div class="contact-label">
      <svg class="icon-phone" viewBox="0 0 20 20"><circle cx="10" cy="10" r="10" fill="#3aab47"/><path d="M7 5l2 2-1 1.5c.6 1.4 1.6 2.4 3 3L12.5 10l2 2-1.2 1.7C9.5 13.5 6.5 10.5 6 6.4z" fill="#fff"/></svg>
      お問合せ
    </div>
    <div class="contact-tel">0952-00-4816</div>
    <a class="btn" href="#">アクセス</a>
  </div>
</header>
<div class="header-rule"></div>

<aside class="sidebar">
  <ul class="global-nav">
    <li>当院のご案内<svg class="arrow" viewBox="0 0 20 20"><circle cx="10" cy="10" r="10" fill="#3aab47"/><path d="M6 8l4 4 4-4" stroke="#fff" stroke-width="2" fill="none"/></svg></li>
    <li>診療のご案内<svg class="arrow" viewBox="0 0 20 20"><circle cx="10" cy="10" r="10" fill="#3aab47"/><path d="M6 8l4 4 4-4" stroke="#fff" stroke-width="2" fill="none"/></svg></li>
    <li>採用のご案内<svg class="arrow" viewBox="0 0 20 20"><circle cx="10" cy="10" r="10" fill="#3aab47"/><path d="M6 8l4 4 4-4" stroke="#fff" stroke-width="2" fill="none"/></svg></li>
    <li>インフォメーション<svg class="arrow" viewBox="0 0 20 20"><circle cx="10" cy="10" r="10" fill="#3aab47"/><path d="M6 8l4 4 4-4" stroke="#fff" stroke-width="2" fill="none"/></svg></li>
  </ul>

  <div class="side-box">
    <h3><svg class="icon-phone" viewBox="0 0 20 20"><circle cx="10" cy="10" r="10" fill="#3aab47"/><path d="M7 5l2 2-1 1.5c.6 1.4 1.6 2.4 3 3L12.5 10l2 2-1.2 1.7C9.5 13.5 6.5 10.5 6 6.4z" fill="#fff"/></svg>お問合せ</h3>
    <div class="side-tel">0952-00-4816</div>
    <div class="map" role="img" aria-label="医院周辺の地図"></div>
    <p class="address">〒840-0000 佐賀県佐賀市若葉町1丁目2-3<br>若葉通り沿い 駐車場完備</p>
    <a class="btn" href="#">大きい地図を見る</a>
  </div>

  <div class="side-box">
    <h3 class="hours-title">診療時間のご案内</h3>
    <table class="hours">
      <tr><th>月曜〜<br>金曜</th><td>10:00〜18:00<br>(昼休憩あり)</td></tr>
      <tr><th>土曜日</th><td>9:30〜18:00<br>(昼休憩あり)</td></tr>
      <tr><th>休診日</th><td>木・日・祝日</td></tr>
    </table>
    <a class="btn" href="#">診療時間を見る</a>
  </div>

  <a class="blog-banner" href="#"><span></span>ブログ</a>
</aside>

<main class="main">
  <h1 class="page-title"><i></i>医院のご紹介</h1>

  <section class="section">
    <h2>当院の診療方針</h2>
    <div class="row">
      <div class="building-photo" role="img" aria-label="医院の外観写真"></div>
      <div class="text">
        <p>当院ではみなさまがいつまでも健康で美しい歯でいられるよう、一人ひとりのお口の状態に合わせた丁寧な診療を心がけています。痛みの少ない治療と分かりやすい説明を大切にし、安心して通っていただける医院づくりに努めております。</p>
        <p>スタッフ一同、地域の皆さまのかかりつけ医として、明るく清潔な環境でお待ちしております。</p>
      </div>
    </div>
    <p class="lead">診療に当たってはカウンセリングを大切にし、予防から治療まで患者さまに合わせたプログラムをご提案いたします。</p>
  </section>

  <section class="section">
    <h2>院長の経歴</h2>
    <div class="row">
      <div>
        <div class="doctor-photo" role="img" aria-label="院長の写真"></div>
        <p class="doctor-note">院長 若葉 拓真<br>佐賀県出身。歯学部卒業後、大学病院での勤務を経て当院を開業。</p>
      </div>
      <ul class="career">
        <li>若葉地区歯科協議会会員</li>
        <li>ひかり口腔研究会会員</li>
        <li>全国予防歯科フォーラム会員</li>
        <li>ルミナ ホワイトニングコース修了</li>
        <li>クレスト矯正コース修了</li>
        <li>ミネル矯正コース修了</li>
        <li>口腔保存研究グループ会員</li>
        <li>ノルデン インプラント基礎コース修了</li>
        <li>ノルデン インプラント応用コース修了</li>
      </ul>
    </div>
  </section>
</main>

<footer class="site-footer">
  <nav class="footer-links">HOME ｜ 当院の診療方針 ｜ 個人情報の取り扱い ｜ サイトマップ</nav>
  <div class="copyright">Copyright (C) 2009 sorvane dental clinic. All Rights Reserved.</div>
</footer>

</body>
</html>
```